Shipping Container Sales & Leasing Flyer

We need a flyer that is going to be presented and left behind while prospecting potential customers. The service we are selling is the sale, rental and customization of 20' and 40' shipping containers.

We provide new and used containers to customers for various reasons, mainly storage. We also custom modify containers into storage units, mobile offices, mobile job site storage, command centers, pump houses, garages, living space, the only limit is the customers imagination.

I would like our company logo and phone / email at the bottom but the design should showcase some of the attached images ive provided as examples and have spots where we can list the types of equipment we have for sale and the various types of conversions we can offer.

Please also tie in to the colour scheme of our logo.

Target Market(s)

Moving & Storage, Construction, Contractors, Business to Business, Any business that needs portable storage, Landscapers, Property Maintenance companies.

Industry/Entity Type

Shipping

Font styles to use
Serif
Sans Serif

Requirements
Must have
• Professional feel, clean original design.
Nice to have
• Tie in to our logo colour scheme.
Should not have
• Bulky or crowded look

```html
<!DOCTYPE html>
<html lang="en">
<head>
<meta charset="UTF-8">
<title>Brennic Management – Shipping Container Flyer</title>
<link rel="stylesheet" href="https://fonts.googleapis.com/css2?family=Cinzel:wght@400;600&family=Montserrat:wght@400;500;700&family=Roboto+Condensed:wght@400;700&display=swap">
<style>
  :root {
    --green: #7cb552;
    --green-dark: #5f9a3c;
    --green-panel: #a9d08a;
    --green-light: #d5e9c3;
    --grey-dark: #3b3b3b;
    --grey-mid: #5d5d5d;
    --grey-light: #8a8a8a;
    --white: #ffffff;
    --ink: #222222;
    --photo-ring: #f4f4f4;
  }
  html, body {
    margin: 0;
    padding: 0;
    width: 900px;
    height: 1200px;
    overflow: hidden;
    background: var(--grey-dark);
  }
  .flyer {
    position: relative;
    width: 900px;
    height: 1200px;
    overflow: hidden;
    font-family: "Montserrat", Arial, sans-serif;
    color: var(--ink);
  }
  .backdrop { position: absolute; inset: 0; }
  .photo { position: absolute; }
  .brand {
    position: absolute;
    left: 40px;
    top: 230px;
    width: 290px;
    text-align: center;
  }
  .brand-mark {
    width: 86px;
    height: 86px;
    border-radius: 50%;
    background: var(--green);
    margin: 0 auto 22px;
  }
  .brand-name {
    font-family: "Montserrat", Arial, sans-serif;
    font-weight: 700;
    color: var(--green-dark);
    font-size: 34px;
    line-height: 1.15;
    letter-spacing: 3px;
    margin: 0;
  }
  .section-title {
    font-family: "Cinzel", Georgia, serif;
    font-weight: 400;
    margin: 0;
    display: inline-block;
    border-bottom: 1.5px solid var(--ink);
  }
  .about { position: absolute; left: 37px; top: 512px; width: 380px; }
  .about .section-title { font-size: 21px; color: var(--ink); padding-right: 12px; }
  .about p { margin: 10px 0 0; font-size: 15.5px; line-height: 1.28; }
  .services-head {
    position: absolute;
    left: 0; top: 633px;
    width: 410px; height: 110px;
    background: var(--green-light);
  }
  .services-head .section-title {
    position: absolute; left: 32px; top: 6px;
    font-size: 34px; font-weight: 600; color: var(--ink); padding-right: 8px;
  }
  .services-head .offer {
    position: absolute; left: 37px; top: 60px;
    font-family: "Roboto Condensed", Arial, sans-serif;
    font-size: 18px; line-height: 1.3; margin: 0; text-transform: uppercase;
  }
  .offer strong { font-weight: 700; }
  .services-body { position: absolute; left: 37px; top: 770px; width: 360px; }
  .services-body .lead { margin: 0; font-size: 17px; line-height: 1.25; }
  .services-body .mods-title {
    margin: 28px 0 0 -4px;
    font-family: "Roboto Condensed", Arial, sans-serif;
    font-weight: 700; font-size: 15.5px;
  }
  .mods {
    list-style: none; margin: 10px 0 0 -16px; padding: 0;
    display: grid; grid-template-columns: 232px 140px;
    grid-auto-flow: column; grid-template-rows: repeat(4, 22px);
    font-family: "Roboto Condensed", Arial, sans-serif; font-weight: 700; font-size: 14.5px;
  }
  .mods li::before { content: "• "; }
  .mods-note {
    margin: 0 0 0 -4px;
    font-family: "Roboto Condensed", Arial, sans-serif; font-weight: 700; font-size: 15px;
  }
  .contact { position: absolute; left: 0; top: 1062px; width: 900px; color: var(--white); }
  .contact .section-title {
    margin-left: 54px; font-size: 20px; color: var(--white); border-color: var(--white); padding-right: 6px;
  }
  .contact-list {
    list-style: none; margin: 0; padding: 0;
    position: absolute; top: 62px; left: 0; width: 900px;
    font-size: 17px; font-weight: 500;
  }
  .contact-list li { position: absolute; display: flex; align-items: center; gap: 7px; white-space: nowrap; }
  .contact-list svg { width: 15px; height: 15px; fill: var(--white); }
</style>
</head>
<body>
<main class="flyer">
  <svg class="backdrop" width="900" height="1200" viewBox="0 0 900 1200" aria-hidden="true">
    <defs>
      <linearGradient id="lowerGrey" x1="0" y1="0" x2="1" y2="1">
        <stop offset="0" stop-color="#7a7a7a"/>
        <stop offset="1" stop-color="#4c4c4c"/>
      </linearGradient>
      <linearGradient id="whitePanel" x1="0" y1="0" x2="1" y2="0">
        <stop offset="0" stop-color="#e9e9e9"/>
        <stop offset="0.6" stop-color="#ffffff"/>
      </linearGradient>
    </defs>
    <rect width="900" height="1200" fill="url(#lowerGrey)"/>
    <polygon points="0,0 900,0 900,330 560,460 0,460" fill="var(--green)"/>
    <polygon points="560,460 900,330 900,560 620,600" fill="#6d6d6d"/>
    <polygon points="0,0 199,0 395,460 0,460" fill="url(#whitePanel)"/>
    <polygon points="0,460 395,460 410,512 0,512" fill="var(--grey-dark)"/>
    <polygon points="395,460 560,460 410,512" fill="#4a4a4a"/>
    <rect x="0" y="512" width="410" height="530" fill="var(--green-panel)"/>
    <path d="M0,1030 C300,1040 600,1045 900,1085 L900,1200 L0,1200 Z" fill="var(--green)"/>
    <path d="M0,1038 C300,1048 600,1053 900,1095 L900,1200 L0,1200 Z" fill="var(--grey-dark)"/>
  </svg>

  <div class="photo" role="img" aria-label="Beige shipping container with a white roll-up door" style="left:567px;top:0;width:333px;height:360px;background:linear-gradient(135deg,#d8c7a4,#c9b48c 55%,#eeeeee);"></div>

  <div class="photo" role="img" aria-label="Blue 20 foot shipping container with closed cargo doors" style="left:370px;top:635px;width:530px;height:430px;background:linear-gradient(135deg,#3f74c8,#1e4e9e 60%,#173d7c);clip-path:polygon(4% 16%,58% 0,100% 8%,100% 92%,58% 100%,4% 82%);"></div>

  <svg class="backdrop" width="900" height="1200" viewBox="0 0 900 1200" aria-hidden="true" style="pointer-events:none">
    <g fill="var(--photo-ring)">
      <circle cx="345" cy="128" r="83"/>
      <circle cx="461" cy="314" r="105"/>
      <circle cx="773" cy="442" r="113"/>
      <circle cx="541" cy="548" r="103"/>
    </g>
  </svg>
  <div class="photo" role="img" aria-label="Row of storage containers with open side doors in a warehouse" style="left:267px;top:50px;width:156px;height:156px;border-radius:50%;background:radial-gradient(circle at 40% 40%,#8a8170,#4f4a40);"></div>
  <div class="photo" role="img" aria-label="White container converted into a mobile office with a glass door" style="left:361px;top:214px;width:200px;height:200px;border-radius:50%;background:linear-gradient(180deg,#d8d6de,#c9cbcf 55%,#6b6b6b);"></div>
  <div class="photo" role="img" aria-label="Blue container with open side storing lumber" style="left:665px;top:334px;width:216px;height:216px;border-radius:50%;background:linear-gradient(180deg,#6b95d2,#3f6fb6 60%,#dfe6ef);"></div>
  <div class="photo" role="img" aria-label="Container interior fitted with white wire shelving units" style="left:443px;top:450px;width:196px;height:196px;border-radius:50%;background:linear-gradient(180deg,#eeeeee,#cfcfcf 65%,#6e4b34);"></div>

  <header class="brand">
    <div class="brand-mark"></div>
    <h1 class="brand-name">BRENNIC<br>MANAGEMENT</h1>
  </header>

  <section class="about">
    <h2 class="section-title">About Us</h2>
    <p>Brennic Management is a professional services firm that is dedicated to providing unique and niche&nbsp; solutions in the transportation &amp; logistics industry.</p>
  </section>

  <section class="services-head">
    <h2 class="section-title">SERVICES</h2>
    <p class="offer"><strong>Sale, rental and customization</strong><br>of 20' and 40' shipping containers</p>
  </section>

  <section class="services-body">
    <p class="lead">We provide new and used containers to&nbsp; customers for various reasons, mainly storage.</p>
    <p class="mods-title">We also custom modify containers into:</p>
    <ul class="mods">
      <li>storage units</li>
      <li>mobile offices</li>
      <li>mobile job site storage</li>
      <li>command centers</li>
      <li>pump houses</li>
      <li>garages</li>
      <li>living space</li>
    </ul>
    <p class="mods-note">the only limit is the customers imagination.</p>
  </section>

  <footer class="contact">
    <h2 class="section-title">Contact Us</h2>
    <ul class="contact-list">
      <li style="left:56px">
        <svg viewBox="0 0 16 16" aria-hidden="true"><path d="M3.6 1.5l2.3 2.6-1.3 1.7c.9 2 2.6 3.7 4.6 4.6l1.7-1.3 2.6 2.3-1.4 2.2C6.8 13.3 2.7 9.2 1.4 3z"/></svg>
        000-0000-000
      </li>
      <li style="left:300px">
        <svg viewBox="0 0 16 16" aria-hidden="true"><path d="M1 4h14v9H1zM2 5l6 4.5L14 5v-.2H2z" fill-rule="evenodd"/></svg>
        your@email.id
      </li>
      <li style="left:563px">
        <svg viewBox="0 0 16 16" aria-hidden="true"><path d="M8 1a7 7 0 100 14A7 7 0 008 1zm0 1.5c.9 1 1.5 2.6 1.7 4.7H6.3C6.5 5.1 7.1 3.5 8 2.5zM2.6 8.8h2.2c.1 1.7.5 3.1 1.1 4.2a5.5 5.5 0 01-3.3-4.2zm0-1.6A5.5 5.5 0 015.9 3c-.6 1.1-1 2.5-1.1 4.2zm5.4 6.3c-.9-1-1.5-2.6-1.7-4.7h3.4c-.2 2.1-.8 3.7-1.7 4.7zm2.1-.5c.6-1.1 1-2.5 1.1-4.2h2.2a5.5 5.5 0 01-3.3 4.2zm1.1-5.8c-.1-1.7-.5-3.1-1.1-4.2a5.5 5.5 0 013.3 4.2z"/></svg>
        your.website.com
      </li>
    </ul>
  </footer>
</main>
</body>
</html>
```